75%-100% OFF - Insulation Banner Design

Need banners created for an online marketing push for my insulation business Velmoor Energy.

www.velmoorenergy.com

Specifically - I would like the banners to pop utilizing our colors in neon. To see samples of colors we use - visit our asset folder.

https://files.quarnex.com/share/7hTkw29plDfa0XbmQzRv4uYc8JnG3sLe?view=open

I will attach sample files to this project.

The banner must highlight 75%-100% off Insulation and Weatherization. If you can include our current perfect Brivvo reviews somewhere in the advertisement that would be awesome but not a requirement.

The banner must meet Kettle Rebate logo guidelines. Please see attachment.

Target Market(s)

Home Owners

Industry/Entity Type

Insulation and Construction

Font styles to use
Sans Serif

Colors
59FF00
82FF00
B8FF75
E3FFCB
F4FFEA

Requirements
Must have
• Kettle Rebate Logo per project description. Must have 75-100% off somewhere that is very clear. And must have our company Velmoor Energy Logo.
Nice to have
• Velmoor Energy Logo

```html
<!DOCTYPE html>
<html lang="en">
<head>
<meta charset="utf-8">
<title>Velmoor Energy – 75%-100% Off Insulation &amp; Weatherization</title>
<link href="https://fonts.googleapis.com/css2?family=Archivo+Black&family=Montserrat:wght@500;700&display=swap" rel="stylesheet">
<style>
  :root {
    --backdrop: #c9e9f8;
    --white: #ffffff;
    --navy: #124b74;
    --navy-deep: #0f4a72;
    --green-start: #4cbb84;
    --teal-mid: #04b3a3;
    --blue-end: #0b86cf;
    --accent-green: #5fae46;
    --earth-brown: #5a3214;
    --skyline-mint: #c9ece6;
  }
  * { margin: 0; padding: 0; box-sizing: border-box; }
  html, body { width: 1200px; height: 386px; overflow: hidden; background: var(--backdrop); }
  .banner {
    position: absolute; left: 21px; top: 45px; width: 1158px; height: 296px;
    overflow: hidden;
    background: linear-gradient(90deg, var(--green-start) 20%, var(--teal-mid) 48%, var(--blue-end) 100%);
    font-family: "Montserrat", sans-serif;
  }
  .brand-panel, .offer { position: absolute; left: 0; top: 0; }
  .skyline {
    position: absolute; left: 340px; right: 0; bottom: 0; height: 42px;
    background: linear-gradient(180deg, rgba(201,236,230,0) 0%, var(--skyline-mint) 70%);
  }
  .company-name {
    position: absolute; left: 34px; top: 44px;
    font-weight: 700; font-size: 40px; line-height: 1.05; color: var(--navy);
  }
  .partner-name {
    position: absolute; left: 34px; top: 226px;
    display: flex; align-items: center; gap: 10px;
    font-weight: 700; font-size: 28px; color: var(--earth-brown);
  }
  .partner-name .dot { width: 22px; height: 22px; border-radius: 50%; background: var(--accent-green); }
  .offer-text { font-family: "Archivo Black", sans-serif; }
  .offer-shadow { fill: var(--accent-green); stroke: var(--navy); stroke-width: 1; }
  .offer-face { fill: var(--white); }
  .service-band { position: absolute; left: 450px; top: 156px; width: 700px; height: 80px; }
  .service-title {
    position: absolute; left: 473px; top: 176px;
    font-weight: 500; font-size: 34px; letter-spacing: 1px; color: var(--white);
    white-space: nowrap;
  }
</style>
</head>
<body>
  <main class="banner">
    <div class="skyline" role="img" aria-label="Pale city skyline silhouette along the bottom edge"></div>

    <svg class="brand-panel" width="1158" height="296" viewBox="0 0 1158 296" aria-hidden="true">
      <polygon points="0,0 231,0 415,188 312,296 0,296" fill="var(--white)"/>
      <polygon points="231,0 245,0 418,178 424,188 418,198 332,296 318,296 412,194 415,188" fill="var(--navy-deep)"/>
    </svg>

    <div class="company-name">Velmoor<br>Energy</div>
    <div class="partner-name"><span class="dot"></span>Kettle Rebate</div>

    <svg class="offer" width="1158" height="160" viewBox="0 0 1158 160" role="img" aria-label="75%-100% OFF">
      <g class="offer-text offer-shadow">
        <text x="437" y="134" font-size="146" textLength="571" lengthAdjust="spacingAndGlyphs">75%-100%</text>
        <text x="1033" y="117" font-size="64" textLength="86" lengthAdjust="spacingAndGlyphs">OFF</text>
      </g>
      <g class="offer-text offer-face">
        <text x="440" y="137" font-size="146" textLength="571" lengthAdjust="spacingAndGlyphs">75%-100%</text>
        <text x="1036" y="120" font-size="64" textLength="86" lengthAdjust="spacingAndGlyphs">OFF</text>
      </g>
    </svg>

    <svg class="service-band" viewBox="0 0 700 80" aria-hidden="true">
      <polygon points="0,0 480,0 472,4 0,4" fill="var(--white)"/>
      <polygon points="0,8 659,8 616,68 0,68" fill="var(--navy)"/>
      <polyline points="487,2 696,2 643,78 390,78" fill="none" stroke="var(--white)" stroke-width="2"/>
      <polygon points="0,76 395,76 388,80 0,80" fill="var(--white)"/>
    </svg>
    <div class="service-title">INSULATION &amp; WEATHERIZATION</div>
  </main>
</body>
</html>
```